Dane Morrow films- wedding and event films company website. DESKTOP AND MOBILE

We need a website for a high-end wedding and event film production company. Looking for a very modern and elegant design. my old website is www.danemorrowfilms.example

I like the "white/black/rose gold" color scheme of my logo.

really looking for a sleek modern design the breaths professional and artistic.

Target Market(s)

wedding and event films.

Industry/Entity Type

Film Production

Number of Pages Required

5+ page

Colors

Designer to choose colors to be used in the design.

Requirements
Must have
• website name will be www.danemorrowfilms.example
• tagline is "CINEMATIC STORIES ABOUT YOU"
• sections: HOME, CONTACT, ABOUT, FILMS, BLOG
• You can see my old website at danemorrowfilms.example
• Website about section:
• Dane Morrow Films was Established with the basis of truly cinematic and artistic films in mind. Dane and his team routinely travel the globe documenting weddings and events for high profile clients and discerning couples. Dane was born and raised in Maui Hawaii and has a unique approach to his films that embody the essence of a Hollywood film. Dane has spent the last 10 years traveling the world documenting corporate events and weddings with multiple Award winning production companies. In 2017 Dane decided to establish his own brand “Dane Morrow films” that will take everything he has learned with his past experiences and push it to the next level. Aside from his personal achievements, Dane is extremely passionate about his craft and always looks forward to handcrafting beautiful wedding/event films for his clients. The style of work is non-traditional and the day of filming is extremely unobtrusive (as we are looking for natural-candid/ raw emotions).
• If you are looking for the best price in town, we are probably not the best option, but if you’re looking for the best quality and peace of mind on your wedding day, then you’re in the right place. Dane Morrow Films is a boutique studio that only accepts a limited number of assignments per year. Inquire early to ensure availability.
• LINKS TO VIMEO VIDEOS THAT WILL BE IN THE "FILMS' SECTION.
• BRENT FILM TRAILER - https://clipvault.example/508114362
• BRENT FEATURE FILM - https://clipvault.example/617392048
• JUNE AND ROB'S WEDDING - https://clipvault.example/724958160
• DRONE DEMO REEL - https://clipvault.example/841576203
• WEDDING INDUSTRY EVENT PARTY - https://clipvault.example/962304817/a8d3e7b21c
• images that you can use on site are here: https://brigittolsenimages.proofbox.example/gallery/nora&felix/
• password is: meadow

```html
<!DOCTYPE html>
<html lang="en">
<head>
<meta charset="utf-8">
<title>Dane Morrow Films</title>
<link rel="stylesheet" href="https://fonts.googleapis.com/css2?family=Poppins:ital,wght@0,200;0,300;0,400;0,500;0,600;0,700;1,300&display=swap">
<style>
:root{
  --rose:#e89a5c;
  --rose-dark:#c9804a;
  --ink:#1f1f1f;
  --text:#4a4a4a;
  --muted:#9a9a9a;
  --line:#dcdcdc;
  --white:#ffffff;
  --dark:#2b2b2b;
}
*{margin:0;padding:0;box-sizing:border-box}
html,body{width:1200px;height:2812px;overflow:hidden;background:var(--white)}
body{position:relative;font-family:'Poppins',sans-serif;color:var(--text)}
.abs{position:absolute}

.bands{position:absolute;left:0;top:0;width:1200px;height:1220px}

/* header */
.brand{left:128px;top:40px;width:210px;display:flex;flex-direction:column;align-items:center;gap:6px}
.brand-mark{width:30px;height:30px;background:var(--rose);align-self:flex-end;margin-right:18px}
.brand-name{font-size:21px;font-weight:500;letter-spacing:1.5px;color:var(--ink);line-height:1}
.brand-sub{font-size:10px;font-weight:500;letter-spacing:5px;color:var(--ink);line-height:1}
.social span{position:absolute;top:33px;width:21px;height:21px;border-radius:50%;background:var(--white);box-shadow:0 1px 3px rgba(0,0,0,.18);display:flex;align-items:center;justify-content:center}
.social span::after{content:"";width:7px;height:7px;border-radius:50%;background:var(--ink)}
.social span.mail::after{display:none}
.nav a{position:absolute;top:87px;font-size:14px;line-height:20px;color:var(--ink);letter-spacing:.2px;text-decoration:none;white-space:nowrap}
.btn{background:var(--rose);color:var(--white);font-weight:600;border-radius:22px;display:flex;align-items:center;justify-content:center;letter-spacing:.5px}
.book-now{left:946px;top:81px;width:126px;height:34px;font-size:14px}

/* hero */
.hero-title{left:128px;top:212px;font-size:49px;line-height:58px;color:#555;font-weight:200;letter-spacing:.5px}
.hero-title strong{display:block;color:var(--rose);font-weight:600}
.hero-copy{left:129px;top:343px;width:420px;font-size:12.5px;line-height:20px;color:#555}

/* about */
.about-title{left:618px;top:772px;font-size:50px;line-height:54px;color:var(--white);font-weight:200;letter-spacing:.5px}
.about-title strong{display:block;font-weight:700}
.about-copy{left:617px;top:895px;width:420px;font-size:12.5px;line-height:20px;color:var(--white)}
.learn-more{left:615px;top:1006px;width:162px;height:44px;font-size:14px}

/* films */
.films-mark{left:256px;top:1216px;width:60px;height:60px;background:var(--rose)}
.films-title{left:126px;top:1290px;font-size:56px;font-weight:300;color:var(--ink);letter-spacing:1px;line-height:1}
.films-copy{left:128px;top:1374px;width:340px;font-size:12.5px;line-height:21px;color:#555}
.films-copy p+p{margin-top:20px}
.film-grid{left:514px;top:1286px;width:558px;height:394px;display:grid;grid-template-columns:1fr 1fr;grid-template-rows:1fr 1fr;gap:3px}
.film-tile{position:relative}
.play{position:absolute;left:110px;top:60px;width:44px;height:44px}
.slider{left:562px;top:1713px;width:476px;height:3px;background:var(--line)}
.slider span{position:absolute;left:27px;top:0;width:118px;height:3px;background:var(--rose)}

/* statement */
.statement{left:0;top:1823px;width:1200px;height:301px;background:linear-gradient(90deg,#1e1e1e,#3a3a3a 55%,#4a4a4a)}
.statement-brand{left:0;top:1882px;width:1200px;text-align:center;color:var(--white)}
.statement-brand .name{font-size:34px;font-weight:300;letter-spacing:4px;line-height:1}
.statement-brand .sub{font-size:13px;letter-spacing:8px;margin-top:6px;display:flex;align-items:center;justify-content:center;gap:14px}
.statement-brand .sub i{display:block;width:70px;height:1px;background:var(--white)}
.statement-copy{left:210px;top:1966px;width:780px;text-align:center;font-size:17px;line-height:25px;color:#e8e8e8;font-weight:300}

/* clients */
.clients-title{left:0;top:2193px;width:1200px;text-align:center;font-size:26px;font-weight:600;color:var(--ink)}
.clients-sub{left:370px;top:2240px;width:460px;text-align:center;font-size:13px;line-height:22px;color:var(--muted)}
.client-card{left:214px;top:2348px;width:306px;height:302px}
.arrow{width:44px;height:44px;border-radius:50%;background:var(--white);box-shadow:0 2px 8px rgba(0,0,0,.18);display:flex;align-items:center;justify-content:center}
.arrow-next{left:486px;top:2387px}
.arrow-prev{left:263px;top:2575px}
.client-name{left:592px;top:2410px;font-size:24px;color:var(--rose);font-weight:400}
.client-quote{left:592px;top:2458px;width:400px;font-size:15.5px;line-height:25px;font-style:italic;font-weight:300;color:#444}
.client-dots{left:592px;top:2525px;display:flex;gap:10px}
.client-dots span{width:18px;height:18px;border-radius:50%;background:#dedede}

.footer{left:0;top:2728px;width:1200px;text-align:center;font-size:14px;font-weight:600;color:var(--ink)}
</style>
</head>
<body>

<svg class="bands" viewBox="0 0 1200 1220">
  <defs>
    <linearGradient id="sky" x1="0" y1="0" x2="0" y2="1">
      <stop offset="0" stop-color="#f5f3f0"/>
      <stop offset=".6" stop-color="#e6ddd3"/>
      <stop offset="1" stop-color="#cfc2b4"/>
    </linearGradient>
    <linearGradient id="cliff" x1="0" y1="0" x2="1" y2="1">
      <stop offset="0" stop-color="#9c9284"/>
      <stop offset="1" stop-color="#5f5a52"/>
    </linearGradient>
    <linearGradient id="band" x1="0" y1="0" x2="1" y2="0">
      <stop offset="0" stop-color="#b8aea2"/>
      <stop offset=".5" stop-color="#cfc6ba"/>
      <stop offset="1" stop-color="#a99f93"/>
    </linearGradient>
    <linearGradient id="portrait" x1="0" y1="0" x2="0" y2="1">
      <stop offset="0" stop-color="#6a6a6a"/>
      <stop offset=".55" stop-color="#3a3a3a"/>
      <stop offset="1" stop-color="#151515"/>
    </linearGradient>
  </defs>
  <g role="img" aria-label="Wedding couple on a seaside cliff at sunset, groom carrying the bride">
    <rect x="0" y="0" width="1200" height="731" fill="url(#sky)"/>
    <polygon points="560,731 760,560 1000,380 1200,0 1200,731" fill="url(#cliff)" opacity=".85"/>
  </g>
  <polygon points="0,562 1200,731 1200,1210 0,1040" fill="url(#band)"/>
  <g role="img" aria-label="Black and white portrait of Daniel Morrow">
    <polygon points="0,600 540,680 540,1115 0,1040" fill="url(#portrait)"/>
  </g>
  <polygon points="0,1040 1200,1210 1200,1220 0,1220" fill="#ffffff"/>
</svg>

<header>
  <div class="abs brand">
    <span class="brand-mark"></span>
    <span class="brand-name">DANE MORROW</span>
    <span class="brand-sub">FILMS</span>
  </div>
  <div class="social" aria-label="Social links">
    <span style="left:907px"></span>
    <span style="left:942px"></span>
    <span style="left:978px"></span>
    <span style="left:1014px"></span>
    <span class="mail" style="left:1047px"><svg width="11" height="8" viewBox="0 0 11 8"><rect x=".5" y=".5" width="10" height="7" fill="none" stroke="#222"/><polyline points=".5,.5 5.5,4.5 10.5,.5" fill="none" stroke="#222"/></svg></span>
  </div>
  <nav class="nav">
    <a style="left:530px">HOME</a>
    <a style="left:609px">CONTACT</a>
    <a style="left:714px">ABOUT</a>
    <a style="left:800px">FILMS</a>
    <a style="left:877px">BLOG</a>
  </nav>
  <div class="abs btn book-now">BOOK NOW</div>
</header>

<section class="hero">
  <h1 class="abs hero-title">CINEMATIC STORIES<strong>ABOUT YOU</strong></h1>
  <p class="abs hero-copy">Dane Morrow Films was Established with the basis of truly cinematic and artistic films in mind. Dane and his team routinely travel the globe documenting weddings and events for high profile clients and discerning couples.</p>
</section>

<section class="about">
  <h2 class="abs about-title"><strong>ABOUT</strong>DANIEL MORROW</h2>
  <p class="abs about-copy">Dane Morrow Films was Established with the basis of truly cinematic and artistic films in mind. Dane and his team routinely travel the globe documenting weddings and events for high profile clients and discerning couples.</p>
  <div class="abs btn learn-more">LEARN MORE</div>
</section>

<section class="films">
  <div class="abs films-mark"></div>
  <h2 class="abs films-title">FILMS</h2>
  <div class="abs films-copy">
    <p>Dane Morrow Films was Established with the basis of truly cinematic and artistic films in mind. Dane and his team routinely travel the globe documenting weddings and events for high profile clients and discerning couples.</p>
    <p>We pride ourselves on using the best quality cinema tools for our films. The equipment we use are industry standard cinematic tools used in hollywood movies, using such tools gives our films a truelly cinematic feel. We work hard to stay up to date with the latest and greatest in our industry and by utilizing the best tools such as 4K Cameras, Gimbals, Jibs, Cranes, and Drones it really sets us apart from the rest.</p>
  </div>
  <div class="abs film-grid">
    <div class="film-tile" role="img" aria-label="Film still: bride and groom on a hillside terrace" style="background:linear-gradient(160deg,#8aa0b0,#b9b2a4 55%,#7f7a70)">
      <svg class="play" viewBox="0 0 44 44"><circle cx="22" cy="22" r="20" fill="none" stroke="#fff" stroke-width="2"/><polygon points="18,14 31,22 18,30" fill="#fff"/></svg>
    </div>
    <div class="film-tile" role="img" aria-label="Film still: couple kissing by the sea" style="background:linear-gradient(180deg,#7e93a6,#3f5d78 60%,#2c4760)"></div>
    <div class="film-tile" role="img" aria-label="Film still: wedding guests under palm trees" style="background:linear-gradient(180deg,#5f7560,#8a8570 55%,#4b4a44)"></div>
    <div class="film-tile" role="img" aria-label="Film still: bridesmaids laughing together" style="background:linear-gradient(180deg,#7a7f7a,#a38574 55%,#6b5a55)"></div>
  </div>
  <div class="abs slider"><span></span></div>
</section>

<section>
  <div class="abs statement" role="img" aria-label="Dark monochrome view of a grand hotel facade with palm trees"></div>
  <div class="abs statement-brand">
    <div class="name">DANE MORROW</div>
    <div class="sub"><i></i>FILMS<i></i></div>
  </div>
  <p class="abs statement-copy">If you are looking for the best price in town, we are probably not the best option, but if you're looking for the best quality and peace of mind on your wedding day, then you're in the right place. Dane Morrow Films is a boutique studio that only accepts a limited number of assignments per year. Inquire early to ensure availability.</p>
</section>

<section class="clients">
  <h2 class="abs clients-title">OUR HAPPY CLIENTS</h2>
  <p class="abs clients-sub">Lorem Ipsum Proin gravida nibh vel velit auctor aliquet. Aenean sollicitudin, lorem quis bibendum auctor.</p>
  <svg class="abs client-card" viewBox="0 0 306 302" role="img" aria-label="Portrait of client Tess Harlow">
    <defs><linearGradient id="client" x1="0" y1="0" x2="0" y2="1"><stop offset="0" stop-color="#f1ede8"/><stop offset="1" stop-color="#d9cfc4"/></linearGradient></defs>
    <polygon points="0,10 306,0 282,302 60,294" fill="url(#client)"/>
  </svg>
  <div class="abs arrow arrow-next"><svg width="10" height="14" viewBox="0 0 10 14"><polyline points="2,1 8,7 2,13" fill="none" stroke="#222" stroke-width="2"/></svg></div>
  <div class="abs arrow arrow-prev"><svg width="10" height="14" viewBox="0 0 10 14"><polyline points="8,1 2,7 8,13" fill="none" stroke="#222" stroke-width="2"/></svg></div>
  <h3 class="abs client-name">Tess Harlow</h3>
  <p class="abs client-quote">"Dane really is one of the best film makers in Hawaii, great work Dane! We loved the film!"</p>
  <div class="abs client-dots"><span></span><span></span></div>
</section>

<footer class="abs footer">©2017 Danemorrow. All Right Reserved.</footer>

</body>
</html>
```